Simple and clean webdesign for personal homepage

Trying to create a simple and clean webdesign for my personal homepage. Going to use a static site builder with templates to build the site. I want it to have multiple pages - like an about me, blog and resume. I just need something very basic I can customize. I want the main colors to be purple, black and white. I am open to other color palettes too but since purple is my favorite color I want that to be one of the main colors.

The site be mostly text driven. Might have some images in the body text but I want the site design to be light and lean.

Industry/Entity Type

Personal Homepage.

Coding

Coded - Design and coding required

Number of Pages Required

1 page

Font styles to use
Sans Serif

Colors
6B429C
8869AF
B7A5CE
E3DAEB
F3F0F8

Requirements
Must have
• Clean design. Purple used as a color. HTML template.
Nice to have
• Responsive

```html
<!DOCTYPE html>
<html lang="en">
<head>
<meta charset="utf-8">
<title>Daniel Harper — Web Designer</title>
<link href="https://fonts.googleapis.com/css2?family=Barlow+Semi+Condensed:wght@500;600;700&family=Poppins:wght@400;500;600&display=swap" rel="stylesheet">
<style>
:root{
  --purple:#6B429C;
  --purple-mid:#8869AF;
  --purple-soft:#B7A5CE;
  --lavender:#E3DAEB;
  --mist:#F3F0F8;
  --ink:#1d1626;
  --text:#5d5668;
  --white:#ffffff;
  --black:#0b0b0d;
}
*{box-sizing:border-box;margin:0;padding:0}
html,body{width:1200px;height:4832px;overflow:hidden}
body{font-family:"Poppins",sans-serif;color:var(--text);background:var(--white);position:relative;font-size:13px;line-height:1.7}
h1,h2,h3,h4,.display{font-family:"Barlow Semi Condensed",sans-serif;color:var(--ink)}
section,header,footer{position:absolute;left:0;width:1200px}
.abs{position:absolute}
.placeholder{position:absolute;border-radius:4px}

/* header / hero */
.hero{top:0;height:608px;background:linear-gradient(120deg,var(--purple) 0%,#7a52aa 60%,var(--purple-mid) 100%)}
.brand{left:160px;top:14px;color:var(--white)}
.brand-mark{font-family:"Barlow Semi Condensed",sans-serif;font-weight:600;font-size:34px;line-height:1}
.brand-name{font-family:"Barlow Semi Condensed",sans-serif;font-weight:600;font-size:11px;letter-spacing:3px;margin-top:2px}
.nav{left:530px;top:30px;display:flex;gap:52px}
.nav a{color:var(--white);text-decoration:none;font-size:12px;font-weight:500;letter-spacing:.5px;position:relative}
.nav a.active::after{content:"";position:absolute;left:0;right:0;bottom:-10px;height:2px;background:var(--white)}
.hello{left:160px;top:120px;border:2px solid var(--white);color:var(--white);font-family:"Barlow Semi Condensed",sans-serif;font-weight:600;font-size:20px;padding:2px 14px;letter-spacing:1px;line-height:1.5}
.hero-title{left:160px;top:174px;color:var(--white);font-size:48px;line-height:1.2;font-weight:500;font-family:"Poppins",sans-serif;letter-spacing:1px}
.hero-copy{left:160px;top:244px;width:420px;color:#ece4f5;font-size:13px;line-height:1.6}
.socials{left:160px;top:312px;display:flex;gap:14px}
.socials span{width:38px;height:38px;border:2px solid var(--white);border-radius:50%;display:block}
.hero-photo{left:760px;top:90px;width:250px;height:518px;background:linear-gradient(180deg,#b9c7dd,#8fa4c4);border-radius:120px 120px 0 0}

/* about */
.about{top:608px;height:552px;background:var(--white)}
.about-shape{left:0;top:330px;width:520px;height:222px;background:var(--purple);border-radius:0 200px 0 0}
.about-photo{left:170px;top:50px;width:300px;height:502px;background:linear-gradient(180deg,#cfc6b9,#9b9180);border-radius:140px 140px 0 0}
.about-name{left:20px;top:432px;color:var(--white);font-family:"Barlow Semi Condensed",sans-serif;font-weight:700;font-size:44px;line-height:1}
.eyebrow{font-size:12px;color:var(--purple);letter-spacing:2px;font-weight:500;display:flex;align-items:center;gap:10px}
.eyebrow::before{content:"";width:30px;height:2px;background:var(--purple)}
.about-eyebrow{left:608px;top:92px}
.about-title{left:608px;top:122px;font-size:40px;font-weight:700;line-height:1.2}
.about-copy{left:608px;top:232px;width:430px;font-size:12px;line-height:1.6}
.about-copy p+p{margin-top:12px}
.btn{display:inline-block;background:var(--purple);color:var(--white);font-size:12px;font-weight:500;padding:9px 26px;border-radius:20px;line-height:1.4}
.about-btn{left:608px;top:424px}

/* section headings */
.sec-head{left:0;width:1200px;text-align:center}
.sec-head .eyebrow{justify-content:center}
.sec-head .eyebrow::after{content:"";width:30px;height:2px;background:var(--purple)}
.sec-head h2{font-size:40px;font-weight:700;margin-top:4px}

/* services */
.services{top:1160px;height:840px;background:var(--mist)}
.services .sec-head{top:74px}
.card{position:absolute;width:280px;height:256px;background:var(--white);text-align:center;padding-top:26px;box-shadow:0 6px 18px rgba(107,66,156,.08);border-bottom:3px solid var(--purple)}
.card .icon{width:60px;height:60px;border-radius:50%;background:var(--purple);margin:0 auto 16px;display:flex;align-items:center;justify-content:center}
.card h3{font-size:22px;font-weight:600;line-height:1.2;margin-bottom:8px}
.card p{font-size:12px;padding:0 26px;line-height:1.6}
.card .more{position:absolute;left:0;right:0;bottom:18px;font-size:12px;line-height:1.4;color:var(--purple);font-weight:500}
.card.featured{background:var(--purple);color:#e9e0f3}
.card.featured h3,.card.featured .more{color:var(--white)}
.card.featured .icon{background:var(--white)}

/* work */
.work{top:2000px;height:760px;background:var(--white)}
.work-eyebrow{left:160px;top:60px}
.work-title{left:160px;top:86px;font-size:40px;font-weight:700}
.work-more{left:940px;top:104px;font-size:13px;color:var(--ink);font-weight:500}
.tile{position:absolute;width:200px;height:208px}
.work-btn{left:530px;top:650px;padding:9px 36px}

/* resume */
.resume{top:2760px;height:800px;background:var(--mist)}
.resume .sec-head{top:60px}
.resume-card{position:absolute;top:160px;width:428px;height:552px;background:var(--white);padding:30px 26px;box-shadow:0 6px 18px rgba(107,66,156,.08)}
.resume-card h3{font-size:28px;font-weight:700;margin-bottom:22px}
.entry{position:relative;padding-left:22px;margin-bottom:26px}
.entry::before{content:"";position:absolute;left:0;top:8px;width:8px;height:8px;border-radius:50%;background:var(--purple)}
.entry h4{font-size:19px;font-weight:600;line-height:1.3}
.entry .date{font-size:11px;color:var(--purple-mid);margin:2px 0 6px}
.entry p{font-size:11.5px;line-height:1.6}

/* blog */
.blog{top:3560px;height:640px;background:var(--white)}
.blog-eyebrow{left:160px;top:72px}
.blog-title{left:160px;top:98px;font-size:40px;font-weight:700}
.blog-btn{left:904px;top:108px;padding:7px 22px}
.post{position:absolute;background:var(--white);box-shadow:0 6px 18px rgba(107,66,156,.1)}
.post h4{font-size:20px;font-weight:600;line-height:1.3}
.post p{font-size:11.5px;line-height:1.6;margin-top:8px}

/* contact */
.contact{top:4200px;height:584px;background:var(--white)}
.contact-title{left:0;width:1200px;top:66px;text-align:center;font-size:40px;font-weight:700;line-height:1.3}
.contact-title span{color:var(--purple)}
.contact-copy{left:330px;top:126px;width:540px;text-align:center;font-size:12px}
.field{position:absolute;border:1px solid var(--lavender);font-size:11px;color:#a49db0;padding:8px 12px;background:var(--white)}
.send{position:absolute;left:192px;top:480px;width:460px;height:38px;background:linear-gradient(90deg,var(--purple),var(--purple-mid));color:var(--white);font-size:13px;text-align:center;line-height:38px}
.info{left:708px;top:192px;width:332px;height:326px;background:var(--purple);border-radius:10px;padding:34px 28px;color:var(--white)}
.info-row{display:flex;gap:18px;margin-bottom:26px}
.info-row .ic{width:44px;height:44px;border-radius:50%;background:var(--white);flex:none;display:flex;align-items:center;justify-content:center}
.info-row b{font-weight:600;font-size:13px;display:block}
.info-row span{font-size:12px;color:#e6dcf2}

footer{top:4784px;height:48px;background:var(--black);color:var(--white);font-size:12px}
.copy{left:160px;top:14px}
.copy span{color:var(--purple-soft)}
.foot-social{left:898px;top:12px;display:flex;gap:10px}
.foot-social span{width:24px;height:24px;border-radius:50%;border:1.5px solid var(--white);display:block}
</style>
</head>
<body>

<header class="hero">
  <div class="abs brand">
    <div class="brand-mark">DH</div>
    <div class="brand-name">DANIEL HARPER</div>
  </div>
  <nav class="abs nav">
    <a class="active">HOME</a><a>ABOUT ME</a><a>BLOG</a><a>RESUME</a><a>CONTACT ME</a>
  </nav>
  <div class="abs hello">HELLO !</div>
  <h1 class="abs hero-title">I Am Web Designer |</h1>
  <p class="abs hero-copy">Lorem ipsum dolor sit amet, consectetuer adipiscing elit, sed diam nonummy nibh euismod tincidunt ut laoreet dolore magna aliquam erat volutpat. Ut wisi enim ad minim.</p>
  <div class="abs socials"><span></span><span></span><span></span><span></span><span></span></div>
  <div class="placeholder hero-photo" role="img" aria-label="Portrait photo of Daniel Harper smiling with arms crossed"></div>
</header>

<section class="about">
  <div class="abs about-shape"></div>
  <div class="placeholder about-photo" role="img" aria-label="Photo of Daniel Harper in a grey suit pointing to the side"></div>
  <div class="abs about-name">Daniel<br>Harper</div>
  <div class="abs eyebrow about-eyebrow">ABOUT ME</div>
  <h2 class="abs about-title">25+ Years Of Experience<br>In Lorem Ipsum</h2>
  <div class="abs about-copy">
    <p>Lorem ipsum dolor sit amet, consectetuer adipiscing elit, sed diam nonummy nibh euismod tincidunt ut laoreet dolore magna aliquam erat volutpat. Ut wisi enim ad minim veniam, quis nostrud exerci tation ullamcorper suscipit lobortis nisl.</p>
    <p>Duis autem vel eum iriure dolor in hendrerit in vulputate velit esse molestie consequat, vel illum dolore eu feugiat nulla facilisis at vero eros et accumsan et iusto odio dignissim qui blandit praesent luptatum.</p>
  </div>
  <span class="abs btn about-btn">Read more</span>
</section>

<section class="services">
  <div class="abs sec-head">
    <div class="eyebrow">MY SKILLS</div>
    <h2>What I Do</h2>
  </div>
  <div class="card" style="left:160px;top:172px">
    <div class="icon"><svg width="26" height="26" viewBox="0 0 26 26" fill="none" stroke="#fff" stroke-width="2"><rect x="3" y="5" width="20" height="13" rx="2"/><path d="M9 22h8M13 18v4"/></svg></div>
    <h3>Service 1</h3><p>Lorem ipsum dolor sit amet, consectetuer adipiscing elit, sed diam nonummy nibh euismod tincidunt.</p><div class="more">Read More &rarr;</div></div>
  <div class="card featured" style="left:460px;top:172px">
    <div class="icon"><svg width="26" height="26" viewBox="0 0 26 26" fill="none" stroke="#6B429C" stroke-width="2"><path d="M4 22V10l9-6 9 6v12z"/><path d="M10 22v-7h6v7"/></svg></div>
    <h3>Service 2</h3><p>Lorem ipsum dolor sit amet, consectetuer adipiscing elit, sed diam nonummy nibh euismod tincidunt.</p><div class="more">Read More &rarr;</div></div>
  <div class="card" style="left:760px;top:172px">
    <div class="icon"><svg width="26" height="26" viewBox="0 0 26 26" fill="none" stroke="#fff" stroke-width="2"><rect x="4" y="4" width="18" height="18" rx="2"/><path d="M8 17l4-5 3 3 3-4"/></svg></div>
    <h3>Service 3</h3><p>Lorem ipsum dolor sit amet, consectetuer adipiscing elit, sed diam nonummy nibh euismod tincidunt.</p><div class="more">Read More &rarr;</div></div>
  <div class="card" style="left:160px;top:468px">
    <div class="icon"><svg width="26" height="26" viewBox="0 0 26 26" fill="none" stroke="#fff" stroke-width="2"><circle cx="13" cy="13" r="8"/><path d="M13 9v4l3 2"/></svg></div>
    <h3>Service 4</h3><p>Lorem ipsum dolor sit amet, consectetuer adipiscing elit, sed diam nonummy nibh euismod tincidunt.</p><div class="more">Read More &rarr;</div></div>
  <div class="card" style="left:460px;top:468px">
    <div class="icon"><svg width="26" height="26" viewBox="0 0 26 26" fill="none" stroke="#fff" stroke-width="2"><path d="M5 8h16M5 13h16M5 18h10"/></svg></div>
    <h3>Service 5</h3><p>Lorem ipsum dolor sit amet, consectetuer adipiscing elit, sed diam nonummy nibh euismod tincidunt.</p><div class="more">Read More &rarr;</div></div>
  <div class="card" style="left:760px;top:468px">
    <div class="icon"><svg width="26" height="26" viewBox="0 0 26 26" fill="none" stroke="#fff" stroke-width="2"><path d="M9 8l-5 5 5 5M17 8l5 5-5 5"/></svg></div>
    <h3>Service 6</h3><p>Lorem ipsum dolor sit amet, consectetuer adipiscing elit, sed diam nonummy nibh euismod tincidunt.</p><div class="more">Read More &rarr;</div></div>
</section>

<section class="work">
  <div class="abs eyebrow work-eyebrow">PROJECT</div>
  <h2 class="abs work-title">My Latest Work</h2>
  <div class="abs work-more">Know More &rarr;</div>
  <div class="tile" style="left:48px;top:180px;background:linear-gradient(160deg,#ffd23f,#f5a623)" role="img" aria-label="Project thumbnail: website landing page illustration in yellow"></div>
  <div class="tile" style="left:272px;top:180px;background:linear-gradient(160deg,#e9eef3,#c9d4e0)" role="img" aria-label="Project thumbnail: marketing landing page illustration"></div>
  <div class="tile" style="left:496px;top:180px;background:linear-gradient(160deg,#ffc36b,#f29c38)" role="img" aria-label="Project thumbnail: online shopping illustration"></div>
  <div class="tile" style="left:48px;top:400px;background:linear-gradient(160deg,#7fe3d0,#3bbfae)" role="img" aria-label="Project thumbnail: teamwork isometric illustration in teal"></div>
  <div class="tile" style="left:272px;top:400px;background:linear-gradient(160deg,#1f5d6e,#0e3344)" role="img" aria-label="Project thumbnail: technology circuit illustration"></div>
  <div class="tile" style="left:496px;top:400px;background:linear-gradient(160deg,#ffe7d6,#ffc9a6)" role="img" aria-label="Project thumbnail: finance app illustration"></div>
  <div class="tile" style="left:728px;top:180px;width:424px;height:428px;background:linear-gradient(140deg,#28d0e6,#6a2fa8 55%,#2b124d)" role="img" aria-label="Featured project: startup business landing page with rocket illustration"></div>
  <span class="abs btn work-btn">Contact Me</span>
</section>

<section class="resume">
  <div class="abs sec-head">
    <div class="eyebrow">EXPERIENCE</div>
    <h2>My Resume</h2>
  </div>
  <div class="resume-card" style="left:160px">
    <h3>My Experience</h3>
    <div class="entry"><h4>Senior Web Developer - Northwind Labs</h4><div class="date">2015 - Present</div><p>Lorem ipsum dolor sit amet, consectetur adipiscing elit. Velit praesentium aut repellendus rem non necessitatibus est dolor illo officiis dignissimos.</p></div>
    <div class="entry"><h4>Mid-Level Web Developer - Northwind Labs</h4><div class="date">2014 - 2015</div><p>Lorem ipsum dolor sit amet, consectetur adipiscing elit. Velit praesentium aut repellendus rem non necessitatibus est dolor illo officiis dignissimos.</p></div>
    <div class="entry"><h4>Junior Web Developer - Northwind Labs</h4><div class="date">2013 - 2014</div><p>Lorem ipsum dolor sit amet, consectetur adipiscing elit. Velit praesentium aut repellendus rem non necessitatibus est dolor illo officiis dignissimos.</p></div>
  </div>
  <div class="resume-card" style="left:612px">
    <h3>My Education</h3>
    <div class="entry"><h4>Engineering Degree - Lakeside University</h4><div class="date">2015 - 2016</div><p>Lorem ipsum dolor sit amet, consectetur adipiscing elit. Velit praesentium aut repellendus rem non necessitatibus est dolor illo officiis dignissimos.</p></div>
    <div class="entry"><h4>Master Degree - Lakeside University</h4><div class="date">2014 - 2015</div><p>Lorem ipsum dolor sit amet, consectetur adipiscing elit. Velit praesentium aut repellendus rem non necessitatibus est dolor illo officiis dignissimos.</p></div>
    <div class="entry"><h4>Bachlor Degree - Lakeside University</h4><div class="date">2013 - 2014</div><p>Lorem ipsum dolor sit amet, consectetur adipiscing elit. Velit praesentium aut repellendus rem non necessitatibus est dolor illo officiis dignissimos.</p></div>
  </div>
</section>

<section class="blog">
  <div class="abs eyebrow blog-eyebrow">BLOG</div>
  <h2 class="abs blog-title">My Blog</h2>
  <span class="abs btn blog-btn">View All Blog</span>
  <article class="post" style="left:160px;top:160px;width:448px;height:330px">
    <div class="placeholder" style="left:0;top:0;width:448px;height:200px;border-radius:0;background:linear-gradient(150deg,#f7c948,#2e5f8a)" role="img" aria-label="Blog photo of a designer working at a desk with a laptop"></div>
    <div style="position:absolute;top:214px;left:20px;right:20px">
      <h4>Lorem Ipsum Dolor Sit Amet Consectetuer Adipiscing</h4>
      <p>Lorem ipsum dolor sit amet, consectetuer adipiscing elit, sed diam nonummy nibh euismod tincidunt ut laoreet.</p>
    </div>
  </article>
  <article class="post" style="left:628px;top:160px;width:412px;height:200px">
    <div class="placeholder" style="left:0;top:0;width:180px;height:200px;border-radius:0;background:linear-gradient(150deg,#f4e3c2,#e0a44f)" role="img" aria-label="Blog photo of a student writing in a notebook"></div>
    <div style="position:absolute;left:196px;top:20px;right:14px"><h4>Lorem Ipsum Dolor Sit Amet Consectetuer</h4><p>Lorem ipsum dolor sit amet, consectetuer adipiscing elit, sed diam nonummy nibh.</p></div>
  </article>
  <article class="post" style="left:628px;top:380px;width:412px;height:200px">
    <div class="placeholder" style="left:0;top:0;width:180px;height:200px;border-radius:0;background:linear-gradient(150deg,#e8d3c3,#b98d78)" role="img" aria-label="Blog photo of colourful pins on a board"></div>
    <div style="position:absolute;left:196px;top:20px;right:14px"><h4>Lorem Ipsum Dolor Sit Amet Consectetuer</h4><p>Lorem ipsum dolor sit amet, consectetuer adipiscing elit, sed diam nonummy nibh.</p></div>
  </article>
</section>

<section class="contact">
  <h2 class="abs contact-title">Get <span>In</span> Touch</h2>
  <p class="abs contact-copy">Lorem ipsum dolor sit amet, consectetuer adipiscing elit, sed diam nonummy nibh euismod tincidunt ut laoreet dolore magna aliquam erat volutpat.</p>
  <div class="field" style="left:192px;top:192px;width:460px;height:36px">Name</div>
  <div class="field" style="left:192px;top:240px;width:224px;height:36px">Email</div>
  <div class="field" style="left:428px;top:240px;width:224px;height:36px">Phone</div>
  <div class="field" style="left:192px;top:288px;width:460px;height:180px">Type your message here</div>
  <div class="send">Send Message</div>
  <div class="abs info">
    <div class="info-row"><div class="ic"><svg width="20" height="20" viewBox="0 0 20 20" fill="#6B429C"><path d="M10 1a6 6 0 0 0-6 6c0 5 6 12 6 12s6-7 6-12a6 6 0 0 0-6-6zm0 8.5A2.5 2.5 0 1 1 10 4.5a2.5 2.5 0 0 1 0 5z"/></svg></div><div><b>Daniel Harper</b><span>48 Maple Lane, Riverton<br>State 012 23 456</span></div></div>
    <div class="info-row"><div class="ic"><svg width="20" height="20" viewBox="0 0 20 20" fill="#6B429C"><path d="M5 2l3 4-2 2a11 11 0 0 0 6 6l2-2 4 3-2 3C9 18 2 11 2 4z"/></svg></div><div><b>Call Us On</b><span>555 014 2298</span></div></div>
    <div class="info-row"><div class="ic"><svg width="20" height="20" viewBox="0 0 20 20" fill="none" stroke="#6B429C" stroke-width="2"><rect x="2" y="4" width="16" height="12" rx="1"/><path d="M2 5l8 6 8-6"/></svg></div><div><b>Email Us On</b><span>hello@danielharper.dev</span></div></div>
  </div>
</section>

<footer>
  <div class="abs copy">Copyright © 2022 <span>Daniel Harper</span>. All Rights Reserved.</div>
  <div class="abs foot-social"><span></span><span></span><span></span><span></span><span></span></div>
</footer>

</body>
</html>
```